Tamkor, a service provider dedicated to improving the performance of a website

Tamkor offers optimization and performance improvement for all types of websites (showcase sites, e-commerce, ...), with the aim of improving their ranking on Vintrel and their customer transformation rate. The main benefits consist in optimizing the factors of a site. In addition, we also offer content creation (description of product sheets, services, ...), Vintrel Ads campaign management, migration version for Prestashop / Wordpress, etc. The design must be a fresh image, dynamic, why not "fun", but also serious. No favorite color, carte blanche on this point;)

```html
<!DOCTYPE html>
<html lang="fr">
<head>
<meta charset="utf-8">
<title>Tamkor – cartes de visite</title>
<link href="https://fonts.googleapis.com/css2?family=Montserrat:wght@300;400;600;700&family=Oswald:wght@600&display=swap" rel="stylesheet">
<style>
  :root {
    --page-bg: #d4d4d4;
    --brand-blue: #3a479c;
    --brand-blue-deep: #233f7c;
    --brand-blue-mid: #34408a;
    --card-white: #ffffff;
    --card-white-shade: #ececec;
    --ink: #222222;
    --text-on-blue: #ffffff;
  }
  * { box-sizing: border-box; margin: 0; padding: 0; }
  html, body { width: 1200px; height: 900px; overflow: hidden; }
  body {
    background: var(--page-bg);
    font-family: "Montserrat", sans-serif;
    position: relative;
  }
  .card {
    position: absolute;
    top: 300px;
    width: 520px;
    height: 300px;
    border-radius: 22px;
    overflow: hidden;
    box-shadow: 0 6px 18px rgba(0,0,0,0.25);
  }
  /* Front side */
  .card--front {
    left: 50px;
    background: var(--brand-blue);
  }
  .card--front .bands { position: absolute; inset: 0; }
  .front-name {
    position: absolute;
    left: 50px;
    top: 122px;
    color: var(--text-on-blue);
    font-weight: 700;
    font-size: 44px;
    letter-spacing: 0.5px;
  }
  .tagline {
    position: absolute;
    left: 276px;
    top: 108px;
    color: var(--text-on-blue);
    font-size: 16px;
    line-height: 1.3;
  }
  .tagline .strong { font-weight: 700; display: block; }
  .tagline .light { font-weight: 300; display: block; }
  /* Back side */
  .card--back {
    left: 630px;
    background: linear-gradient(180deg, var(--card-white-shade) 0%, var(--card-white) 45%);
  }
  .back-logo {
    position: absolute;
    left: 48px;
    top: 122px;
    color: var(--brand-blue);
    font-weight: 700;
    font-size: 44px;
  }
  .divider {
    position: absolute;
    left: 252px;
    top: 86px;
    width: 2px;
    height: 128px;
    background: var(--brand-blue);
    opacity: 0.8;
  }
  .contact {
    position: absolute;
    left: 274px;
    top: 86px;
  }
  .contact-name {
    font-family: "Oswald", sans-serif;
    font-weight: 600;
    font-size: 24px;
    color: var(--brand-blue);
    line-height: 1.1;
  }
  .contact-role {
    font-size: 15px;
    color: var(--ink);
    margin-bottom: 12px;
  }
  .contact-line {
    display: flex;
    align-items: center;
    gap: 8px;
    font-size: 14px;
    color: var(--ink);
    line-height: 1.6;
  }
  .contact-line svg { width: 13px; height: 13px; flex: none; }
</style>
</head>
<body>

  <section class="card card--front" aria-label="Recto de la carte">
    <svg class="bands" viewBox="0 0 520 300" preserveAspectRatio="none" aria-hidden="true">
      <polygon points="0,0 520,0 520,30 0,190" fill="var(--brand-blue-mid)"/>
      <polygon points="130,130 520,95 520,300 210,300" fill="var(--brand-blue-deep)"/>
    </svg>
    <div class="front-name">Tamkor</div>
    <p class="tagline">
      <span class="strong">Un site</span>
      <span class="strong">internet performant</span>
      <span class="light">pour</span>
      <span class="light">Vintrel et les internautes</span>
    </p>
  </section>

  <section class="card card--back" aria-label="Verso de la carte">
    <div class="back-logo">Tamkor</div>
    <div class="divider"></div>
    <div class="contact">
      <div class="contact-name">JULIEN MARCHAND</div>
      <div class="contact-role">Founder</div>
      <div class="contact-line">
        <svg viewBox="0 0 16 16" aria-hidden="true"><path d="M4 1l3 3-2 2c1 2 3 4 5 5l2-2 3 3-2 3C7 15 1 9 1 3z" fill="var(--brand-blue)"/></svg>
        06 21 57 93 40
      </div>
      <div class="contact-line">
        <svg viewBox="0 0 16 16" aria-hidden="true"><rect x="1" y="3" width="14" height="10" fill="none" stroke="var(--brand-blue)" stroke-width="1.6"/><path d="M1 3l7 6 7-6" fill="none" stroke="var(--brand-blue)" stroke-width="1.6"/></svg>
        julien@tamkor.fr
      </div>
      <div class="contact-line">
        <svg viewBox="0 0 16 16" aria-hidden="true"><circle cx="8" cy="8" r="6.5" fill="none" stroke="var(--brand-blue)" stroke-width="1.5"/><ellipse cx="8" cy="8" rx="3" ry="6.5" fill="none" stroke="var(--brand-blue)" stroke-width="1.2"/><path d="M1.5 8h13" stroke="var(--brand-blue)" stroke-width="1.2"/></svg>
        www.tamkor.fr
      </div>
    </div>
  </section>

</body>
</html>
```